Business Cards for new orthopaedic surgery practice

My husband and I are starting our own orthopaedic surgery practice. We are looking for a business card that is uniform, but one will have my name/title and the other will have his. You can just create one design with my name on it for now. But when I choose your design as the winning design I will ask that you add another copy with his name/title.

We are looking for classy, simple, elite all in one. We like dark blues/a little gold/yellow. Something that goes with our logo. We want our logo incorporated. Here is all the info you need:
Business name: RV Spine & Vitality Center
Location: 38915 North Bramble Ave
Marlow Heights, FL 33490
Phone: 954-218-4630
Fax: 954-571-2846
Email: info@myrvspine.example

Names: Lucinda Ferrow, M.D.
Board Certified Hand and Upper Extremity Surgeon

Emeka Dlunga, M.D.
Board Certified Hip & Knee Replacement/General Orthopaedic Surgeon

Can decide what you want to put on the back. Maybe a slogan:
Grounded in Care. Built Around You

I am just going to upload our logo. The only thing is if we select you as the winning design, the location, and phone numbers may change. We will need your help to update that once fully solidified.

Industry/Entity Type

Medical

Contact Information for Business Card

Colors
0054AA
0677BA
7BADD7
CADEEF
E8F1F8
0094D4
00A9DD
6FCCEA
C7EBF8
E9F6FB

Requirements
Must have
• class, appeal,
Should not have
• We want to air on the side of masculine if we are looking at masculine vs. feminine feel. But we still want it classy, sophisticated, and something we will love

```html
<!DOCTYPE html>
<html lang="en">
<head>
<meta charset="utf-8">
<title>RV Spine &amp; Vitality Center — Business Card</title>
<link rel="stylesheet" href="https://fonts.googleapis.com/css2?family=Cinzel:wght@600&family=Playfair+Display:wght@800&family=Montserrat:wght@400;500&family=Cormorant+Garamond:wght@500&display=swap">
<style>
  :root {
    --bg: #ebe8e4;
    --navy: #111d47;
    --navy-emboss: #3a4677;
    --gold: #c49a45;
    --ink-grey: #4a4d57;
    --paper: #fbfbfa;
  }
  * { margin: 0; padding: 0; box-sizing: border-box; }
  html, body { width: 1200px; height: 960px; overflow: hidden; }
  body {
    background: var(--bg);
    display: flex;
    flex-direction: column;
    align-items: center;
    justify-content: center;
    gap: 60px;
  }
  .card {
    position: relative;
    width: 700px;
    height: 400px;
    box-shadow: 0 6px 18px rgba(0,0,0,0.12);
  }
  /* Front */
  .card-front { background: var(--navy); }
  .brand-mark {
    position: absolute;
    display: flex;
    align-items: center;
    gap: 14px;
    font-family: "Cinzel", serif;
    font-weight: 600;
    letter-spacing: 0.12em;
    text-transform: uppercase;
  }
  .brand-mark .dot {
    flex: none;
    border-radius: 50%;
    border: 2px solid currentColor;
  }
  .card-front .brand-mark {
    left: 50%; top: 50%;
    transform: translate(-50%, -58%);
    width: 340px;
    color: var(--navy-emboss);
    font-size: 26px;
    line-height: 1.3;
  }
  .card-front .brand-mark .dot { width: 34px; height: 34px; }
  .slogan {
    position: absolute;
    left: 44px; bottom: 36px;
    font-family: "Cormorant Garamond", serif;
    font-weight: 500;
    font-size: 14px;
    letter-spacing: 0.14em;
    text-transform: uppercase;
    color: var(--gold);
  }
  /* Back */
  .card-back { background: var(--paper); }
  .card-back .brand-mark {
    right: 44px; top: 48px;
    width: 300px;
    color: var(--navy);
    font-size: 22px;
    line-height: 1.3;
  }
  .card-back .brand-mark .dot { width: 30px; height: 30px; }
  .details {
    position: absolute;
    left: 46px; top: 168px;
  }
  .doctor-name {
    font-family: "Playfair Display", serif;
    font-weight: 800;
    font-size: 24px;
    letter-spacing: 0.02em;
    color: var(--navy);
    text-transform: uppercase;
  }
  .doctor-title {
    margin-top: 6px;
    font-family: "Montserrat", sans-serif;
    font-weight: 500;
    font-size: 15px;
    line-height: 1.3;
    color: var(--gold);
  }
  .address, .contact {
    font-family: "Montserrat", sans-serif;
    font-size: 14px;
    line-height: 1.38;
    color: var(--ink-grey);
  }
  .address { margin-top: 12px; }
  .contact { list-style: none; margin-top: 4px; }
  .contact li { display: flex; align-items: center; gap: 8px; }
  .contact svg { width: 13px; height: 13px; fill: var(--navy); flex: none; }
</style>
</head>
<body>

  <section class="card card-front" aria-label="Card front">
    <div class="brand-mark"><span class="dot"></span><span>RV Spine &amp; Vitality Center</span></div>
    <p class="slogan">Grounded in Care. Built Around You</p>
  </section>

  <section class="card card-back" aria-label="Card back">
    <div class="brand-mark"><span class="dot"></span><span>RV Spine &amp; Vitality Center</span></div>
    <div class="details">
      <h1 class="doctor-name">Lucinda Ferrow, M.D.</h1>
      <p class="doctor-title">Board Certified Hand<br>and Upper Extremity Surgeon</p>
      <p class="address">RV Spine &amp; Vitality Center<br>38915 North Bramble Ave<br>Marlow Heights, FL 33490</p>
      <ul class="contact">
        <li><svg viewBox="0 0 16 16" aria-label="Phone"><path d="M3 1h3l1.5 4-2 1.2a9 9 0 0 0 4.3 4.3L11 8.5l4 1.5v3a2 2 0 0 1-2 2A13 13 0 0 1 1 3a2 2 0 0 1 2-2z"/></svg>954-218-4630</li>
        <li><svg viewBox="0 0 16 16" aria-label="Fax"><path d="M4 1h7v4H4zM2 6h12a1 1 0 0 1 1 1v6H1V7a1 1 0 0 1 1-1zm2 5v4h8v-4z"/></svg>954-571-2846</li>
        <li><svg viewBox="0 0 16 16" aria-label="Email"><path d="M1 3h14v1L8 9 1 4zm0 3 7 5 7-5v7H1z"/></svg>info@myrvspine.example</li>
      </ul>
    </div>
  </section>

</body>
</html>
```